Business Card for Brevel Coatings

We need a simple, yet out standing business card for our painting company.

Target Market(s)

wealthy; high-end neighborhoods, and businesses

Industry/Entity Type

Painting

Contact Information for Business Card

Name:
Doran Vask

Email:
d.vask@brevel-coatings.com

Website:
Brevel-coatings.com

Phone Number:
(555) 416-9073

Font styles to use
Serif
Sans Serif

Requirements
Must have
• slogan "making change simple"
Should not have
• A title attached to the name on the card

```html
<!DOCTYPE html>
<html lang="en">
<head>
<meta charset="utf-8">
<title>Brevel Coatings — Business Card</title>
<link rel="stylesheet" href="https://fonts.googleapis.com/css2?family=Fira+Sans:wght@400;600&display=swap">
<style>
  :root {
    --page: #ffffff;
    --lime: #b7cf42;
    --forest: #3d5226;
  }
  html, body {
    margin: 0;
    padding: 0;
    width: 1200px;
    height: 1100px;
    overflow: hidden;
    background: var(--page);
  }
  .canvas {
    position: relative;
    width: 1200px;
    height: 1100px;
  }
  .card {
    position: absolute;
    left: 75px;
    top: 250px;
    width: 1050px;
    height: 600px;
    background: var(--lime);
    overflow: hidden;
  }
  .card__panel {
    position: absolute;
    inset: 0;
  }
  .brand {
    position: absolute;
    left: 360px;
    top: 255px;
    display: flex;
    align-items: center;
    gap: 14px;
    font-family: "Fira Sans", sans-serif;
    font-weight: 600;
    font-size: 42px;
    color: var(--forest);
    letter-spacing: 0.5px;
  }
  .brand__dot {
    width: 22px;
    height: 22px;
    border-radius: 50%;
    background: var(--forest);
  }
  .website {
    position: absolute;
    left: 0;
    right: 0;
    top: 520px;
    text-align: center;
    padding-left: 48px;
    font-family: "Fira Sans", sans-serif;
    font-size: 36px;
    font-weight: 400;
    color: var(--forest);
    letter-spacing: 0.5px;
  }
  .website__name {
    font-weight: 600;
  }
</style>
</head>
<body>
<main class="canvas">
  <section class="card">
    <svg class="card__panel" width="1050" height="600" viewBox="0 0 1050 600">
      <defs>
        <linearGradient id="brushFade" x1="0" y1="0" x2="1" y2="0">
          <stop offset="0" stop-color="#3d5226" stop-opacity="0.9"/>
          <stop offset="1" stop-color="#3d5226" stop-opacity="0.15"/>
        </linearGradient>
      </defs>
      <polygon class="card__shade" fill="var(--forest)"
               points="0,0 300,0 262,55 210,140 160,250 145,330 70,470 0,590"/>
      <polygon class="card__brush" role="img" aria-label="Dry brush stroke sweeping diagonally across the card"
               fill="url(#brushFade)"
               points="300,0 470,20 420,70 370,150 330,230 300,320 260,400 230,470 170,510 160,420 150,330 160,250 210,140 262,55"/>
    </svg>
    <div class="brand">
      <span class="brand__dot"></span>
      <span class="brand__name">Brevel Coatings</span>
    </div>
    <p class="website"><span class="website__name">Brevel</span>-coatings.com</p>
  </section>
</main>
</body>
</html>
```